4th Generation Family Business Needs a New Card Design!

We are a family owned 4th Generation company. We are based in the Sydney, Australia area and we are desperately in need of a more modern and classy card. We are monumental masons who design, supply & erect lasting memorials throughout cemeteries in Sydney. Our customers are normally in a period of grieving. I have attached logo files that will need to be implemented on the card. Company was established 1935. Australian Owned and Operated. Card needs to be designed to PRINTLY.com specification.

Target Market(s)

Our target market is based upon people that a grieving for family members that have passed away. We also deal with alot of companies that own and operate cemeteries.

Industry/Entity Type

Business

Contact Information for Business Card

Oliver Brantley, Operations Manager, 0417552908, oliver@hollowaystoneworks.com.au
Martin Brantley, Director, 0431906627, martin@hollowaystoneworks.com.au
Phone # 02 9634 2258
Website: www.hollowaystoneworks.com.au
Address: Suite 17, 8 Calloway Lane, East Penrose, Sydney NSW 2290

Font styles to use
Serif
Decorative
Script

Requirements
Must have
• Would like to see the logo nicely implemented with a modern design. Embossed lettering would be a nice additive.

```html
<!DOCTYPE html>
<html lang="en">
<head>
<meta charset="utf-8">
<title>Holloway Stoneworks – Business Card</title>
<link rel="stylesheet" href="https://fonts.googleapis.com/css2?family=Montserrat:wght@400;500;700&display=swap">
<style>
  :root {
    --backdrop: #2b2b2d;
    --card: #050505;
    --gold: #f2c12e;
    --white: #ffffff;
    --muted: #e6e6e6;
    --divider: #5a5a5a;
  }
  * { box-sizing: border-box; margin: 0; padding: 0; }
  html, body { width: 1200px; height: 900px; overflow: hidden; }
  body {
    background: var(--backdrop);
    font-family: "Montserrat", Arial, sans-serif;
    position: relative;
  }
  .card {
    position: absolute;
    width: 560px;
    height: 320px;
    background: var(--card);
    border-radius: 18px;
    overflow: hidden;
    box-shadow: 0 14px 30px rgba(0,0,0,.45);
  }
  .card--front { left: 120px; top: 100px; }
  .card--back  { left: 520px; top: 480px; }

  .card__bands { position: absolute; left: 0; bottom: 0; width: 560px; height: 40px; }

  .brand-name {
    color: var(--white);
    font-weight: 700;
    letter-spacing: 2px;
    text-transform: uppercase;
    text-align: center;
    line-height: 1.15;
  }
  .card--front .brand-name {
    position: absolute; left: 0; right: 0; top: 92px;
    font-size: 34px;
  }
  .card--front .brand-rule {
    position: absolute; left: 190px; right: 190px; top: 188px;
    height: 2px; background: var(--gold);
  }
  .web-line {
    position: absolute; right: 60px; bottom: 52px;
    color: var(--white); font-size: 15px; font-weight: 500;
  }
  .web-line strong { color: var(--gold); font-weight: 700; }

  .card--back .brand-block {
    position: absolute; left: 24px; top: 95px; width: 220px;
  }
  .card--back .brand-name { font-size: 24px; }
  .card--back .brand-mark {
    width: 14px; height: 14px; background: var(--gold);
    margin: 14px auto 0;
  }
  .card__divider {
    position: absolute; left: 262px; top: 62px; width: 1px; height: 170px;
    background: var(--divider);
  }
  .contact {
    position: absolute; left: 278px; right: 22px; top: 44px;
    color: var(--muted);
  }
  .contact__name { color: var(--gold); font-size: 22px; font-weight: 700; }
  .contact__role { font-size: 12.5px; margin-top: 2px; }
  .contact__address { font-size: 12.5px; line-height: 1.4; margin-top: 8px; }
  .contact__list { list-style: none; margin-top: 6px; }
  .contact__list li {
    display: flex; align-items: center; gap: 8px;
    font-size: 12.5px; line-height: 1.5;
    white-space: nowrap;
  }
  .contact__list svg { width: 11px; height: 11px; flex: none; }
  .contact__list strong { color: var(--gold); font-weight: 700; }
</style>
</head>
<body>

  <section class="card card--front">
    <div class="brand-name">Holloway<br>Stoneworks</div>
    <div class="brand-rule"></div>
    <p class="web-line">www.<strong>hollowaystoneworks</strong>.com.au</p>
    <svg class="card__bands" viewBox="0 0 560 40" aria-hidden="true">
      <polygon points="0,28 330,28 322,40 0,40" fill="var(--white)"/>
      <polygon points="340,16 560,16 560,30 333,30" fill="var(--gold)"/>
    </svg>
  </section>

  <section class="card card--back">
    <div class="brand-block">
      <div class="brand-name">Holloway<br>Stoneworks</div>
      <div class="brand-mark"></div>
    </div>
    <div class="card__divider"></div>
    <div class="contact">
      <h1 class="contact__name">Martin Brantley</h1>
      <p class="contact__role">Director</p>
      <p class="contact__address">Suite 17, 8 Calloway Lane<br>East Penrose, Sydney NSW 2290</p>
      <ul class="contact__list">
        <li>
          <svg viewBox="0 0 12 12"><rect x="3" y="0.5" width="6" height="11" rx="1.2" fill="none" stroke="var(--gold)" stroke-width="1.3"/><circle cx="6" cy="9.5" r=".8" fill="var(--gold)"/></svg>
          0431906627
        </li>
        <li>
          <svg viewBox="0 0 12 12"><path d="M2.5 1 L4.5 1 L5.3 3.6 L4 4.6 Q5 7 7.4 8 L8.4 6.7 L11 7.5 L11 9.5 Q10.5 11 9 11 Q1 10 1 2.5 Q1 1 2.5 1Z" fill="var(--gold)"/></svg>
          02 9634 2258
        </li>
        <li>
          <svg viewBox="0 0 12 12"><rect x="0.7" y="2.2" width="10.6" height="7.6" fill="none" stroke="var(--gold)" stroke-width="1.2"/><path d="M1 2.6 L6 6.6 L11 2.6" fill="none" stroke="var(--gold)" stroke-width="1.2"/></svg>
          martin@hollowaystoneworks.com.au
        </li>
        <li>
          <svg viewBox="0 0 12 12"><circle cx="6" cy="6" r="5" fill="none" stroke="var(--gold)" stroke-width="1.2"/><ellipse cx="6" cy="6" rx="2" ry="5" fill="none" stroke="var(--gold)" stroke-width="1"/><line x1="1" y1="6" x2="11" y2="6" stroke="var(--gold)" stroke-width="1"/></svg>
          <span>www.<strong>hollowaystoneworks</strong>.com.au</span>
        </li>
      </ul>
    </div>
    <svg class="card__bands" viewBox="0 0 560 40" aria-hidden="true">
      <polygon points="0,28 330,28 322,40 0,40" fill="var(--white)"/>
      <polygon points="340,16 560,16 560,30 333,30" fill="var(--gold)"/>
    </svg>
  </section>

</body>
</html>
```